KORBALT

The business want a professional looking business card. We have a scetch we will add but want the extra upgrade, and would like more suggestions for variations of our business cards.

```html
<!DOCTYPE html>
<html lang="en">
<head>
<meta charset="UTF-8">
<title>KORBALT – Business Card</title>
<link rel="stylesheet" href="https://fonts.googleapis.com/css2?family=Marcellus&family=Montserrat:wght@400;500&display=swap">
<style>
  :root {
    --page-bg: #f0efed;
    --card-dark: #281c15;
    --card-cream: #f5ead9;
    --gold: #c4a574;
    --ink: #221812;
  }
  * { margin: 0; padding: 0; box-sizing: border-box; }
  html, body {
    width: 1200px;
    height: 670px;
    overflow: hidden;
    background: var(--page-bg);
  }
  .canvas {
    position: relative;
    width: 1200px;
    height: 670px;
  }
  .card {
    position: absolute;
    left: 347px;
    width: 507px;
    height: 301px;
  }

  /* Front side */
  .card-front {
    top: 22px;
    background: var(--card-dark);
    color: var(--gold);
    text-align: center;
  }
  .brand-dot {
    position: absolute;
    left: 50%;
    top: 76px;
    width: 56px;
    height: 56px;
    margin-left: -28px;
    border-radius: 50%;
    background: var(--gold);
  }
  .brand-name {
    position: absolute;
    left: 0;
    right: 0;
    top: 168px;
    font-family: "Marcellus", serif;
    font-size: 44px;
    line-height: 1;
    letter-spacing: 0.28em;
    padding-left: 0.28em;
  }
  .brand-since {
    position: absolute;
    left: 0;
    right: 0;
    top: 225px;
    font-family: "Montserrat", sans-serif;
    font-weight: 500;
    font-size: 13px;
    letter-spacing: 0.42em;
    padding-left: 0.42em;
  }

  /* Back side */
  .card-back {
    top: 347px;
    background: var(--card-cream);
    color: var(--ink);
  }
  .person-name {
    position: absolute;
    left: 60px;
    top: 44px;
    font-family: "Marcellus", serif;
    font-size: 43px;
    line-height: 1;
  }
  .person-role {
    position: absolute;
    left: 61px;
    top: 95px;
    font-family: "Montserrat", sans-serif;
    font-size: 19px;
  }
  .contact-list {
    position: absolute;
    left: 59px;
    top: 164px;
    list-style: none;
    font-family: "Montserrat", sans-serif;
    font-size: 20px;
  }
  .contact-item {
    display: flex;
    align-items: center;
    height: 32.5px;
  }
  .contact-icon {
    width: 20px;
    height: 20px;
    margin-right: 15px;
    flex-shrink: 0;
  }
  .mini-brand {
    position: absolute;
    left: 384px;
    width: 100px;
    top: 204px;
    text-align: center;
    color: var(--gold);
  }
  .mini-brand-dot {
    width: 26px;
    height: 26px;
    margin: 0 auto 9px;
    border-radius: 50%;
    background: var(--gold);
  }
  .mini-brand-name {
    font-family: "Marcellus", serif;
    font-size: 11.5px;
    letter-spacing: 0.2em;
    padding-left: 0.2em;
    line-height: 1;
  }
  .mini-brand-since {
    font-family: "Montserrat", sans-serif;
    font-size: 4.5px;
    letter-spacing: 0.4em;
    padding-left: 0.4em;
    margin-top: 3px;
  }
</style>
</head>
<body>
<main class="canvas">

  <section class="card card-front" aria-label="Card front">
    <div class="brand-dot"></div>
    <h1 class="brand-name">KORBALT</h1>
    <p class="brand-since">SINCE 2026</p>
  </section>

  <section class="card card-back" aria-label="Card back">
    <h2 class="person-name">Anders Halvor Brekke</h2>
    <p class="person-role">CEO &amp; Founder</p>

    <ul class="contact-list">
      <li class="contact-item">
        <svg class="contact-icon" viewBox="0 0 20 20" aria-hidden="true">
          <rect x="5" y="1" width="10" height="18" rx="2" fill="none" stroke="var(--ink)" stroke-width="1.6"/>
          <line x1="8.5" y1="3.5" x2="11.5" y2="3.5" stroke="var(--ink)" stroke-width="1"/>
          <circle cx="10" cy="16" r="1" fill="var(--ink)"/>
        </svg>
        <span>004790556172</span>
      </li>
      <li class="contact-item">
        <svg class="contact-icon" viewBox="0 0 20 20" aria-hidden="true">
          <rect x="1" y="4" width="18" height="12" fill="var(--ink)"/>
          <polyline points="1.5,4.5 10,11 18.5,4.5" fill="none" stroke="var(--card-cream)" stroke-width="1.3"/>
          <polyline points="1.5,15.5 7.5,9.5 M18.5,15.5 12.5,9.5" fill="none" stroke="var(--card-cream)" stroke-width="1.1"/>
          <line x1="1.5" y1="15.5" x2="7.5" y2="9.5" stroke="var(--card-cream)" stroke-width="1.1"/>
          <line x1="18.5" y1="15.5" x2="12.5" y2="9.5" stroke="var(--card-cream)" stroke-width="1.1"/>
        </svg>
        <span>korbalt.llc@mailbox.com</span>
      </li>
      <li class="contact-item">
        <svg class="contact-icon" viewBox="0 0 20 20" aria-hidden="true">
          <circle cx="10" cy="10" r="8.5" fill="none" stroke="var(--ink)" stroke-width="1.5"/>
          <ellipse cx="10" cy="10" rx="4" ry="8.5" fill="none" stroke="var(--ink)" stroke-width="1"/>
          <line x1="1.5" y1="10" x2="18.5" y2="10" stroke="var(--ink)" stroke-width="1"/>
          <line x1="3" y1="5.5" x2="17" y2="5.5" stroke="var(--ink)" stroke-width="1"/>
          <line x1="3" y1="14.5" x2="17" y2="14.5" stroke="var(--ink)" stroke-width="1"/>
        </svg>
        <span>www.korbalt.llc</span>
      </li>
    </ul>

    <div class="mini-brand">
      <div class="mini-brand-dot"></div>
      <p class="mini-brand-name">KORBALT</p>
      <p class="mini-brand-since">SINCE 2026</p>
    </div>
  </section>

</main>
</body>
</html>
```